Spinning Wheel: Spin & Win

We are looking to design a large sticker cover for a spinning wheel (please see attached reference)

Wheel diameter: 120 cm (1.2meters)

Divided into 8 sections:
1- Free Meal
2- Tolvik Gift Card
3- Haircut or Blowdry
4- Tolvik Gift Card
5- Merchandise
6- Tolvik Gift Card
7- Meal voucher
8- Tolvik Gift Card

Text in the center:
Buy for 200 AED to Spin & Win!
(Spin & Win should be the most dominant visually)

Font: Something classy and elegant (maybe cursive but easily read)

Colors: Khaki - All shades of brown and dark brown (note: the wheel structure is made of wood that is dark brown)

Feel: Wood and Old Paper
Updates

Target Market(s)

Upper Class

Industry/Entity Type

Graphic Design

Font styles to use
Decorative
Script

Requirements
Should not have
• Flashy colors

```html
<!DOCTYPE html>
<html lang="en">
<head>
<meta charset="utf-8">
<title>Spin &amp; Win Wheel</title>
<link rel="stylesheet" href="https://fonts.googleapis.com/css2?family=Libre+Caslon+Text:wght@700&family=Rye&display=swap">
<style>
  :root {
    --khaki: #a99a5b;
    --olive: #5d5a2f;
    --tan: #ad7851;
    --walnut: #673a1e;
    --cream: #f3e9bd;
    --ink: #4a2a13;
    --gold-light: #f2dc94;
    --gold: #c9a64e;
    --gold-deep: #7d5f1f;
    --paper: #f1eecd;
  }
  html, body {
    margin: 0;
    padding: 0;
    width: 1200px;
    height: 1000px;
    overflow: hidden;
  }
  body {
    background: linear-gradient(to bottom, #ffffff 0%, #ffffff 78%, #e4e4e4 100%);
  }
  .wheel {
    display: block;
    width: 1200px;
    height: 1000px;
  }
  .prize-label {
    font-family: "Libre Caslon Text", "Times New Roman", serif;
    font-weight: 700;
    fill: var(--cream);
    text-anchor: middle;
    filter: drop-shadow(2px 3px 2px rgba(40, 20, 5, 0.55));
  }
  .prize-label .line-main { font-size: 50px; }
  .prize-label .line-sub { font-size: 42px; }
  .prize-number {
    font-family: "Libre Caslon Text", "Times New Roman", serif;
    font-weight: 700;
    font-size: 44px;
    fill: var(--cream);
    text-anchor: middle;
    filter: drop-shadow(2px 3px 2px rgba(40, 20, 5, 0.55));
  }
  .hub-offer {
    font-family: "Libre Caslon Text", "Times New Roman", serif;
    font-weight: 700;
    font-size: 27px;
    fill: var(--ink);
    stroke: var(--gold-light);
    stroke-width: 1.5px;
    paint-order: stroke;
    text-anchor: middle;
  }
  .hub-headline {
    font-family: "Rye", "Georgia", serif;
    font-size: 62px;
    fill: var(--ink);
    stroke: var(--cream);
    stroke-width: 5px;
    paint-order: stroke;
    text-anchor: middle;
    filter: drop-shadow(3px 4px 3px rgba(30, 15, 5, 0.6));
  }
</style>
</head>
<body>
<svg class="wheel" viewBox="0 0 1200 1000" xmlns="http://www.w3.org/2000/svg" role="img" aria-label="Spin and win prize wheel with eight sections">
  <defs>
    <radialGradient id="rim-gold" cx="50%" cy="50%" r="50%">
      <stop offset="90%" stop-color="var(--gold-deep)"/>
      <stop offset="94%" stop-color="var(--gold-light)"/>
      <stop offset="97%" stop-color="var(--gold)"/>
      <stop offset="100%" stop-color="var(--gold-deep)"/>
    </radialGradient>
    <linearGradient id="rim-sheen" x1="0" y1="0" x2="1" y2="1">
      <stop offset="0%" stop-color="#fff3c4" stop-opacity="0.6"/>
      <stop offset="50%" stop-color="#fff3c4" stop-opacity="0"/>
      <stop offset="100%" stop-color="#3a2a08" stop-opacity="0.35"/>
    </linearGradient>
    <radialGradient id="sector-shade" cx="50%" cy="50%" r="50%">
      <stop offset="30%" stop-color="#000" stop-opacity="0"/>
      <stop offset="100%" stop-color="#1c0d02" stop-opacity="0.35"/>
    </radialGradient>
    <radialGradient id="hub-paper" cx="45%" cy="40%" r="60%">
      <stop offset="0%" stop-color="#fbf8e2"/>
      <stop offset="100%" stop-color="var(--paper)"/>
    </radialGradient>
    <path id="sector" d="M600 478 L456.5 131.6 A375 375 0 0 1 743.5 131.6 Z"/>
  </defs>

  <!-- outer rim -->
  <g class="rim">
    <circle cx="600" cy="478" r="412" fill="url(#rim-gold)"/>
    <circle cx="600" cy="478" r="412" fill="url(#rim-sheen)"/>
    <circle cx="600" cy="478" r="399" fill="none" stroke="var(--gold-deep)" stroke-width="6" stroke-dasharray="2 8" opacity="0.7"/>
    <circle cx="600" cy="478" r="384" fill="var(--gold-deep)"/>
    <circle cx="600" cy="478" r="380" fill="none" stroke="var(--gold-light)" stroke-width="3"/>
  </g>

  <!-- prize sectors -->
  <g class="sectors">
    <use href="#sector" fill="var(--khaki)" transform="rotate(0 600 478)"/>
    <use href="#sector" fill="var(--olive)" transform="rotate(45 600 478)"/>
    <use href="#sector" fill="var(--tan)" transform="rotate(90 600 478)"/>
    <use href="#sector" fill="var(--walnut)" transform="rotate(135 600 478)"/>
    <use href="#sector" fill="var(--khaki)" transform="rotate(180 600 478)"/>
    <use href="#sector" fill="var(--olive)" transform="rotate(225 600 478)"/>
    <use href="#sector" fill="var(--tan)" transform="rotate(270 600 478)"/>
    <use href="#sector" fill="var(--walnut)" transform="rotate(315 600 478)"/>
    <circle cx="600" cy="478" r="375" fill="url(#sector-shade)"/>
  </g>

  <!-- dividers -->
  <g class="dividers" stroke="var(--gold-light)" stroke-width="4">
    <line x1="600" y1="478" x2="456.5" y2="131.6" transform="rotate(0 600 478)"/>
    <line x1="600" y1="478" x2="456.5" y2="131.6" transform="rotate(45 600 478)"/>
    <line x1="600" y1="478" x2="456.5" y2="131.6" transform="rotate(90 600 478)"/>
    <line x1="600" y1="478" x2="456.5" y2="131.6" transform="rotate(135 600 478)"/>
    <line x1="600" y1="478" x2="456.5" y2="131.6" transform="rotate(180 600 478)"/>
    <line x1="600" y1="478" x2="456.5" y2="131.6" transform="rotate(225 600 478)"/>
    <line x1="600" y1="478" x2="456.5" y2="131.6" transform="rotate(270 600 478)"/>
    <line x1="600" y1="478" x2="456.5" y2="131.6" transform="rotate(315 600 478)"/>
  </g>

  <!-- prize labels -->
  <g class="prize" transform="rotate(0 600 478)">
    <text class="prize-label"><tspan class="line-main" x="607" y="178">Free</tspan><tspan class="line-main" x="607" y="232">Meal</tspan></text>
    <text class="prize-number" x="607" y="325">1</text>
  </g>
  <g class="prize" transform="rotate(45 600 478)">
    <text class="prize-label"><tspan class="line-main" x="600" y="178">Tolvik</tspan><tspan class="line-sub" x="600" y="228">Gift Card</tspan></text>
    <text class="prize-number" x="600" y="325">2</text>
  </g>
  <g class="prize" transform="rotate(90 600 478)">
    <text class="prize-label"><tspan class="line-sub" x="600" y="178">Haircut or</tspan><tspan class="line-sub" x="600" y="228">Blowdry</tspan></text>
    <text class="prize-number" x="600" y="325">3</text>
  </g>
  <g class="prize" transform="rotate(135 600 478)">
    <text class="prize-label"><tspan class="line-main" x="600" y="178">Tolvik</tspan><tspan class="line-sub" x="600" y="228">Gift Card</tspan></text>
    <text class="prize-number" x="600" y="325">4</text>
  </g>
  <g class="prize" transform="rotate(180 600 478)">
    <text class="prize-label"><tspan class="line-main" x="600" y="178">Merchan-</tspan><tspan class="line-main" x="600" y="230">dise</tspan></text>
    <text class="prize-number" x="600" y="325">5</text>
  </g>
  <g class="prize" transform="rotate(225 600 478)">
    <text class="prize-label"><tspan class="line-main" x="600" y="178">Tolvik</tspan><tspan class="line-sub" x="600" y="228">Gift Card</tspan></text>
    <text class="prize-number" x="600" y="325">6</text>
  </g>
  <g class="prize" transform="rotate(270 600 478)">
    <text class="prize-label"><tspan class="line-main" x="600" y="178">Meal</tspan><tspan class="line-sub" x="600" y="228">Voucher</tspan></text>
    <text class="prize-number" x="600" y="325">7</text>
  </g>
  <g class="prize" transform="rotate(315 600 478)">
    <text class="prize-label"><tspan class="line-main" x="600" y="178">Tolvik</tspan><tspan class="line-sub" x="600" y="228">Gift Card</tspan></text>
    <text class="prize-number" x="600" y="325">8</text>
  </g>

  <!-- center hub -->
  <g class="hub">
    <circle cx="606" cy="490" r="112" fill="#2a1608" opacity="0.55" filter="blur(6px)"/>
    <circle cx="604" cy="486" r="110" fill="url(#hub-paper)"/>
    <g transform="rotate(-20 604 486)">
      <text class="hub-offer" x="604" y="442">Buy for</text>
      <text class="hub-offer" x="604" y="474">200 AED to</text>
      <text class="hub-headline" x="604" y="536">SPIN &amp;</text>
      <text class="hub-headline" x="610" y="592">WIN!</text>
    </g>
  </g>
</svg>
</body>
</html>
```